TALVORIK

The business want a professional looking business card. We have a scetch we will add but want the extra upgrade, and would like more suggestions for variations of our business cards.

```html
<!DOCTYPE html>
<html lang="en">
<head>
<meta charset="utf-8">
<title>TALVORIK — Business Card</title>
<link rel="stylesheet" href="https://fonts.googleapis.com/css2?family=Playfair+Display:wght@700&family=Cormorant+Garamond:ital,wght@1,500&family=Montserrat:wght@400;500&display=swap">
<style>
  :root {
    --backdrop: #7b7a7c;
    --gold-light: #f3ead2;
    --gold-mid: #dccaa0;
    --gold-deep: #b89a5e;
    --ink: #8a6a2c;
    --ink-dark: #6f5320;
    --line: #c2a463;
  }
  * { margin: 0; padding: 0; box-sizing: border-box; }
  html, body { width: 1200px; height: 902px; overflow: hidden; }
  body {
    background: var(--backdrop);
    position: relative;
    font-family: "Montserrat", sans-serif;
    color: var(--ink);
  }
  .card {
    position: absolute;
    top: 281px;
    width: 540px;
    height: 340px;
    border-radius: 4px;
    overflow: hidden;
    background: linear-gradient(135deg, var(--gold-light) 0%, var(--gold-mid) 55%, var(--gold-deep) 100%);
    box-shadow: 0 18px 40px rgba(0,0,0,.28);
  }
  .card--front { left: 40px; }
  .card--back { left: 620px; }
  .card__curves { position: absolute; inset: 0; width: 100%; height: 100%; }

  .contact { position: absolute; left: 34px; top: 34px; }
  .contact__brand {
    font-family: "Playfair Display", serif;
    font-weight: 700;
    font-size: 40px;
    letter-spacing: 1px;
    color: var(--ink-dark);
    line-height: 1;
  }
  .contact__surname {
    font-size: 19px;
    font-weight: 500;
    letter-spacing: 5px;
    color: var(--ink-dark);
    margin-top: 4px;
  }
  .contact__rule { width: 46px; height: 1px; background: var(--ink); margin: 12px 0 10px; }
  .contact__role { font-size: 10px; letter-spacing: 3px; }
  .contact__name {
    font-family: "Cormorant Garamond", serif;
    font-style: italic;
    font-weight: 500;
    font-size: 21px;
    margin: 4px 0 16px;
  }
  .contact__list { list-style: none; }
  .contact__item {
    display: flex; align-items: center; gap: 12px;
    font-size: 13px; letter-spacing: .6px; margin-bottom: 9px;
  }
  .contact__icon {
    width: 20px; height: 20px; border-radius: 50%;
    background: var(--ink); display: flex; align-items: center; justify-content: center;
  }

  .wordmark { position: absolute; text-align: center; color: var(--ink); }
  .wordmark__dot { width: 34px; height: 34px; border-radius: 50%; background: var(--ink); margin: 0 auto 10px; }
  .wordmark__name {
    font-family: "Playfair Display", serif; font-weight: 700;
    line-height: 1; letter-spacing: 1px; color: var(--ink-dark);
  }
  .wordmark__tagline {
    display: flex; align-items: center; justify-content: center; gap: 10px;
    font-size: 9px; letter-spacing: 4px; margin-top: 6px;
  }
  .wordmark__tagline::before, .wordmark__tagline::after {
    content: ""; width: 26px; height: 1px; background: var(--ink);
  }
  .card--front .wordmark { left: 330px; top: 96px; width: 190px; }
  .card--front .wordmark__name { font-size: 32px; }
  .card--back .wordmark { left: 0; right: 0; top: 96px; }
  .card--back .wordmark__dot { width: 46px; height: 46px; }
  .card--back .wordmark__name { font-size: 50px; }
  .card--back .wordmark__tagline { font-size: 11px; }
</style>
</head>
<body>
  <section class="card card--front">
    <svg class="card__curves" viewBox="0 0 540 340" aria-hidden="true">
      <line x1="360" y1="28" x2="292" y2="312" stroke="var(--line)" stroke-width="1"/>
      <path d="M540 160 C470 240 420 300 300 340" fill="none" stroke="#f7eccd" stroke-width="1.4"/>
      <path d="M540 190 C480 260 430 310 350 340" fill="none" stroke="var(--line)" stroke-width="1.2"/>
      <path d="M380 340 C420 290 470 270 540 262" fill="none" stroke="#f7eccd" stroke-width="1.2"/>
    </svg>
    <div class="contact">
      <div class="contact__brand">TALVORIK</div>
      <div class="contact__surname">HÅVIK</div>
      <div class="contact__rule"></div>
      <div class="contact__role">CEO &amp; FOUNDER</div>
      <div class="contact__name">Anders Lund Håvik</div>
      <ul class="contact__list">
        <li class="contact__item"><span class="contact__icon"><svg width="10" height="10" viewBox="0 0 10 10"><path d="M2 1 L4 1 L4.6 3 L3.4 3.8 C4 5.2 4.8 6 6.2 6.6 L7 5.4 L9 6 L9 8 C5 8.5 1.5 5 2 1Z" fill="#f3ead2"/></svg></span>004790114726</li>
        <li class="contact__item"><span class="contact__icon"><svg width="11" height="8" viewBox="0 0 11 8"><rect x=".5" y=".5" width="10" height="7" fill="none" stroke="#f3ead2"/><path d="M.5 .5 L5.5 4.5 L10.5 .5" fill="none" stroke="#f3ead2"/></svg></span>talvorik.llc@mailbox.com</li>
        <li class="contact__item"><span class="contact__icon"><svg width="11" height="11" viewBox="0 0 11 11"><circle cx="5.5" cy="5.5" r="4.6" fill="none" stroke="#f3ead2"/><ellipse cx="5.5" cy="5.5" rx="2" ry="4.6" fill="none" stroke="#f3ead2"/><line x1=".9" y1="5.5" x2="10.1" y2="5.5" stroke="#f3ead2"/></svg></span>www.talvorik.llc</li>
      </ul>
    </div>
    <div class="wordmark">
      <div class="wordmark__dot"></div>
      <div class="wordmark__name">TALVORIK</div>
      <div class="wordmark__tagline">SINCE 2026</div>
    </div>
  </section>

  <section class="card card--back">
    <svg class="card__curves" viewBox="0 0 540 340" aria-hidden="true">
      <path d="M0 250 C60 190 120 100 150 0" fill="none" stroke="#f7eccd" stroke-width="1.4"/>
      <path d="M0 280 C70 220 130 120 175 0" fill="none" stroke="var(--line)" stroke-width="1.2"/>
      <path d="M540 60 C470 120 420 240 390 340" fill="none" stroke="#f7eccd" stroke-width="1.4"/>
      <path d="M540 90 C480 150 440 250 420 340" fill="none" stroke="var(--line)" stroke-width="1.2"/>
    </svg>
    <div class="wordmark">
      <div class="wordmark__dot"></div>
      <div class="wordmark__name">TALVORIK</div>
      <div class="wordmark__tagline">SINCE 2026</div>
    </div>
  </section>
</body>
</html>
```